Logo and Packaging for Low Dose Full Spectrum Cannabis Extract Capsules - Marlowe Co

Hi! I am hoping to get a logo and packaging design for low dose (2, 5, and 10mg) full spectrum cannabis extract capsules.

Overall we are going for a natural, healthy, earthy. clean, safe, trustworthy, environmentally friendly look and would love to use lots of natural colors like brown and green as well as white.

For the Marlowe Co logo I would love to have something clean and simple, possibly involving a stylized capsule or plant/leaf.

The labels will be printed on 8x2" (203.2 x 50.8 mm) paper bands that will wrap around the 3.125" (79.4 mm) wide fronts and backs of white tin containers -the sides are 0.5625” (14.3 mm). There will be a 0.5" (12.7 mm) of overlap at the end of the band that will be covered by the adhesive.

Designs should include the following information:

Front:
- Marlowe Co logo (not the main focus)
- X mg THC per capsule (final versions with 2, 5, and 10 and this should be relatively prominent. The capsules get darker as they get to higher strengths and it might be nice to represent that on the labels as well)
- Indica, Sativa, or Hybrid (maybe Purple for Indica, Green for Sativa, and a third color for Hybrid?)
- 15 Full Spectrum Cannabis Extract Capsules

Back:
- For adult use only. Keep away from children.
- This product has not been analyzed or evaluated by the QVR
- Ingredients: Olive oil, full spectrum cannabis extract, gelatin capsules
- Made in DC

Wealthy young professionals between 25 and 55, especially women, for the woman who has it all as a discreet and classy alternative to sleep aids, other herbal supplements, or a glass of Pinot noir

Serif
Sans Serif
• Garamond, Lucida Bright, Georgia, Goudy, Bangkok, Brooklyn, Sage

```html
<!DOCTYPE html>
<html lang="en">
<head>
<meta charset="utf-8">
<title>Marlowe Co — Capsule Tin Bands</title>
<link rel="stylesheet" href="https://fonts.googleapis.com/css2?family=Montserrat:wght@300;400;600;700;800&family=Open+Sans:wght@300;400;700&family=Oswald:wght@300&display=swap">
<style>
  :root {
    --backdrop: #b3b3b3;
    --paper: #ffffff;
    --ink: #1a1a1a;
    --indica: #46187a;
    --indica-edge: #5a2585;
    --indica-soft: #8a40f0;
    --sativa: #248c25;
    --sativa-edge: #137019;
    --sativa-soft: #7cbf48;
    --hybrid: #ee7600;
    --hybrid-edge: #ec5e00;
    --hybrid-soft: #f6a040;
  }
  * { margin: 0; padding: 0; box-sizing: border-box; }
  html, body { width: 1200px; height: 989px; overflow: hidden; }
  body { background: var(--backdrop); position: relative; font-family: "Open Sans", sans-serif; }

  .band {
    position: absolute; left: 51px; width: 1090px; height: 272px;
    background: var(--tone); overflow: hidden;
    box-shadow: 0 2px 4px rgba(0,0,0,.25);
  }
  .band--indica { top: 60px;  --tone: var(--indica); --edge: var(--indica-edge); --soft: var(--indica-soft); }
  .band--sativa { top: 354px; --tone: var(--sativa); --edge: var(--sativa-edge); --soft: var(--sativa-soft); }
  .band--hybrid { top: 652px; --tone: var(--hybrid); --edge: var(--hybrid-edge); --soft: var(--hybrid-soft); }

  .up   { position: absolute; writing-mode: vertical-rl; transform: rotate(180deg); text-align: start; white-space: nowrap; }
  .down { position: absolute; writing-mode: vertical-rl; white-space: nowrap; }

  .band__overlap { position: absolute; left: 0; top: 0; width: 23px; height: 100%; background: var(--paper); }
  .band__blank {
    left: 110px; top: 28px; width: 40px; height: 214px;
    font-family: "Oswald", sans-serif; font-weight: 300; font-size: 42px; line-height: 40px;
    color: var(--soft); letter-spacing: .3px;
  }

  .front { position: absolute; left: 239px; top: 0; width: 425px; height: 100%;
    background: linear-gradient(90deg, var(--edge) 0, var(--tone) 60px); }
  .front__card {
    position: absolute; left: 25px; top: 48px; width: 359px; height: 240px;
    background: var(--paper); border-radius: 28px 28px 0 0;
    border: 5px solid #6d6d6d; border-bottom: 0;
    border-color: #555 #bbb #bbb #555;
  }
  .front__brand { left: 61px; top: 58px; width: 26px; height: 190px;
    font-family: "Montserrat", sans-serif; font-weight: 800; font-size: 23px; line-height: 26px; color: var(--ink); }
  .front__dose { left: 193px; top: 98px; width: 46px; height: 150px;
    font-family: "Montserrat", sans-serif; font-weight: 600; font-size: 18px; line-height: 23px; color: var(--ink); }
  .front__strain { left: 251px; top: 112px; width: 44px; height: 136px;
    font-family: "Montserrat", sans-serif; font-weight: 800; font-size: 34px; line-height: 40px;
    color: var(--tone); border-left: 2px solid var(--tone); border-right: 2px solid var(--tone); }
  .front__count { left: 330px; top: 60px; width: 36px; height: 188px;
    font-family: "Open Sans", sans-serif; font-weight: 400; font-size: 14px; line-height: 18px; color: var(--ink); }
  .front__badge { left: 393px; top: 130px; width: 24px; height: 118px;
    font-family: "Montserrat", sans-serif; font-weight: 800; font-size: 18px; line-height: 24px; color: var(--paper);
    display: flex; align-items: center; gap: 4px; }
  .front__badge-num { display: inline-flex; align-items: center; justify-content: center;
    width: 22px; height: 22px; border-radius: 50%; background: var(--paper); color: var(--tone);
    font-size: 12px; line-height: 1; writing-mode: horizontal-tb; transform: rotate(90deg); }

  .band__seam { position: absolute; left: 664px; top: 0; width: 18px; height: 100%;
    background: linear-gradient(90deg, #6a6a6a, #c8c8c8 50%, #6a6a6a); }

  .back { position: absolute; left: 682px; top: 0; width: 408px; height: 100%; color: var(--paper); }
  .back__brand { left: 362px; top: 80px; width: 24px; height: 150px;
    font-family: "Montserrat", sans-serif; font-weight: 800; font-size: 20px; line-height: 24px; }
  .back__molecule { position: absolute; left: 252px; top: 51px; width: 96px; height: 171px;
    background: linear-gradient(180deg, rgba(255,255,255,.14), rgba(255,255,255,.06)); border-radius: 6px; }
  .back__story { left: 201px; top: 36px; width: 36px; height: 200px; text-align: center;
    font-weight: 300; font-size: 9.5px; line-height: 11.5px; }
  .back__ingredients { left: 163px; top: 44px; width: 25px; height: 186px;
    font-weight: 700; font-size: 9.5px; line-height: 12px; }
  .back__rule { position: absolute; left: 148px; top: 40px; width: 1px; height: 194px; background: var(--paper); }
  .back__facility { left: 115px; top: 42px; width: 22px; height: 190px;
    font-weight: 400; font-size: 9px; line-height: 11px; }
  .back__pill { left: 86px; top: 62px; width: 17px; height: 152px; border-radius: 9px;
    background: var(--paper); color: var(--tone); font-weight: 700; font-size: 9.5px; line-height: 17px;
    display: flex; align-items: center; justify-content: center; }
  .back__storage { left: 59px; top: 54px; width: 14px; height: 170px;
    font-weight: 400; font-size: 10px; line-height: 14px; text-transform: uppercase; }
  .back__origin { left: 25px; top: 72px; width: 18px; height: 110px;
    font-family: "Montserrat", sans-serif; font-weight: 700; font-size: 13px; line-height: 18px;
    display: flex; align-items: center; gap: 6px; }
  .back__pin { writing-mode: horizontal-tb; width: 14px; height: 16px; }
</style>
</head>
<body>

<section class="band band--indica">
  <div class="band__overlap"></div>
  <div class="up band__blank">BLANK SPACE</div>
  <div class="front">
    <div class="front__card"></div>
    <div class="up front__brand">MARLOWE CO</div>
    <div class="up front__dose">10MG THC<br>PER CAPSULE</div>
    <div class="up front__strain">INDICA</div>
    <div class="up front__count">15 Full Spectrum<br>Cannabis Extract Capsules</div>
    <div class="up front__badge"><span class="front__badge-num">15</span>CAPSULES</div>
  </div>
  <div class="band__seam"></div>
  <div class="back">
    <div class="down back__brand">MARLOWE CO</div>
    <div class="back__molecule" role="img" aria-label="Line diagram of the THC molecule"></div>
    <div class="down back__story">Our capsules are made from full spectrum<br>laboratory-tested extracts of high quality<br>cannabis flower</div>
    <div class="down back__ingredients">Ingredients: Olive oil, full spectrum<br>cannabis extract, gelatin capsules</div>
    <div class="back__rule"></div>
    <div class="down back__facility">Prepared in a facility that also processes<br>peanuts, tree nuts, milk, eggs, and soy</div>
    <div class="down back__pill">Sugar Free and Gluten Free</div>
    <div class="down back__storage">Store in a cool dry place</div>
    <div class="down back__origin"><svg class="back__pin" viewBox="0 0 14 16" aria-hidden="true"><path d="M7 0C3.4 0 1 2.6 1 5.8 1 10 7 16 7 16s6-6 6-10.2C13 2.6 10.6 0 7 0z" fill="#fff"/></svg>Made in DC</div>
  </div>
</section>

<section class="band band--sativa">
  <div class="band__overlap"></div>
  <div class="up band__blank">BLANK SPACE</div>
  <div class="front">
    <div class="front__card" style="left:19px"></div>
    <div class="up front__brand" style="left:55px">MARLOWE CO</div>
    <div class="up front__dose" style="left:187px">10MG THC<br>PER CAPSULE</div>
    <div class="up front__strain" style="left:245px">SATIVA</div>
    <div class="up front__count" style="left:324px">15 Full Spectrum<br>Cannabis Extract Capsules</div>
    <div class="up front__badge" style="left:387px"><span class="front__badge-num">15</span>CAPSULES</div>
  </div>
  <div class="band__seam"></div>
  <div class="back">
    <div class="down back__brand">MARLOWE CO</div>
    <div class="back__molecule" role="img" aria-label="Line diagram of the THC molecule"></div>
    <div class="down back__story">Our capsules are made from full spectrum<br>laboratory-tested extracts of high quality<br>cannabis flower</div>
    <div class="down back__ingredients">Ingredients: Olive oil, full spectrum<br>cannabis extract, gelatin capsules</div>
    <div class="back__rule"></div>
    <div class="down back__facility">Prepared in a facility that also processes<br>peanuts, tree nuts, milk, eggs, and soy</div>
    <div class="down back__pill">Sugar Free and Gluten Free</div>
    <div class="down back__storage">Store in a cool dry place</div>
    <div class="down back__origin"><svg class="back__pin" viewBox="0 0 14 16" aria-hidden="true"><path d="M7 0C3.4 0 1 2.6 1 5.8 1 10 7 16 7 16s6-6 6-10.2C13 2.6 10.6 0 7 0z" fill="#fff"/></svg>Made in DC</div>
  </div>
</section>

<section class="band band--hybrid">
  <div class="band__overlap"></div>
  <div class="up band__blank">BLANK SPACE</div>
  <div class="front">
    <div class="front__card"></div>
    <div class="up front__brand">MARLOWE CO</div>
    <div class="up front__dose">10MG THC<br>PER CAPSULE</div>
    <div class="up front__strain">HYBRID</div>
    <div class="up front__count">15 Full Spectrum<br>Cannabis Extract Capsules</div>
    <div class="up front__badge"><span class="front__badge-num">15</span>CAPSULES</div>
  </div>
  <div class="band__seam"></div>
  <div class="back">
    <div class="down back__brand">MARLOWE CO</div>
    <div class="back__molecule" role="img" aria-label="Line diagram of the THC molecule"></div>
    <div class="down back__story">Our capsules are made from full spectrum<br>laboratory-tested extracts of high quality<br>cannabis flower</div>
    <div class="down back__ingredients">Ingredients: Olive oil, full spectrum<br>cannabis extract, gelatin capsules</div>
    <div class="back__rule"></div>
    <div class="down back__facility">Prepared in a facility that also processes<br>peanuts, tree nuts, milk, eggs, and soy</div>
    <div class="down back__pill">Sugar Free and Gluten Free</div>
    <div class="down back__storage">Store in a cool dry place</div>
    <div class="down back__origin"><svg class="back__pin" viewBox="0 0 14 16" aria-hidden="true"><path d="M7 0C3.4 0 1 2.6 1 5.8 1 10 7 16 7 16s6-6 6-10.2C13 2.6 10.6 0 7 0z" fill="#fff"/></svg>Made in DC</div>
  </div>
</section>

</body>
</html>
```